Postcard Design

We are a landscape maintenance, design and build company. Our services include weekly property maintenance, spring and fall clean ups, tree, shrub and plant care, pool renovations and new installations, patio and retaining wall design and construction, deign and building of outdoor kitchens, fireplaces and water features.we are a fully insured NJ Home Improvement Contractor License 27KP81926058

It Company

```html
<!DOCTYPE html>
<html lang="en">
<head>
<meta charset="utf-8">
<title>K&amp;R Contracting Postcard</title>
<link href="https://fonts.googleapis.com/css2?family=Jost:wght@400;500&amp;family=Tinos:wght@700&amp;display=swap" rel="stylesheet">
<style>
  :root {
    --green: #3aaa35;
    --green-dark: #1f8a2c;
    --green-light: #6cc24a;
    --ink: #222222;
    --grey-text: #4a4a4a;
    --paper: #ffffff;
    --paper-soft: #f2f2f2;
    --paper-shade: #e6e6e6;
    --backdrop: #2b2624;
    --photo-stone: #a88a6e;
    --photo-leaf: #4f7a3a;
    --photo-water: #3d7fc4;
  }
  * { box-sizing: border-box; margin: 0; padding: 0; }
  html, body { width: 900px; height: 1200px; overflow: hidden; }
  body { background: var(--backdrop); font-family: "Jost", sans-serif; position: relative; }

  .postcard { position: absolute; left: 98px; width: 704px; height: 545px; overflow: hidden; }
  .postcard--front { top: 36px; background: linear-gradient(180deg, var(--paper) 40%, var(--paper-soft) 100%); }
  .postcard--back { top: 623px; background: linear-gradient(90deg, var(--paper-shade) 0%, var(--paper) 45%); }

  .card-art { position: absolute; inset: 0; }

  .headline { position: absolute; right: 34px; top: 200px; text-align: right; font-family: "Tinos", serif; font-weight: 700; color: var(--ink); }
  .headline__lead { font-size: 36px; line-height: 40px; }
  .headline__sub { font-size: 21px; line-height: 29px; margin-top: 4px; }

  .credentials { position: absolute; right: 34px; top: 308px; text-align: right; font-size: 21px; line-height: 30px; color: var(--grey-text); letter-spacing: 0.2px; }

  .brand-box { position: absolute; left: 41px; top: 363px; width: 166px; height: 163px; background: var(--paper); border: 3px solid var(--green); display: flex; flex-direction: column; align-items: center; justify-content: center; text-align: center; padding: 6px; }
  .brand-box__mark { width: 30px; height: 30px; background: var(--green-dark); border-radius: 50%; margin-bottom: 6px; }
  .brand-name { font-family: "Tinos", serif; font-weight: 700; color: var(--green-dark); }
  .brand-name__short { display: block; font-size: 34px; line-height: 36px; }
  .brand-name__long { display: block; font-size: 15px; line-height: 18px; letter-spacing: 0.5px; }
  .brand-tagline { font-family: "Tinos", serif; font-weight: 700; font-size: 10px; color: var(--ink); margin-top: 6px; }
  .brand-phone { font-family: "Tinos", serif; font-weight: 700; font-size: 13px; color: var(--ink); }

  .services-tab { position: absolute; left: 0; top: 25px; width: 224px; height: 34px; background: var(--green); clip-path: polygon(0 0, 88% 0, 100% 100%, 0 100%); color: var(--paper); font-size: 23px; font-weight: 400; line-height: 34px; padding-left: 40px; }
  .services-list { position: absolute; left: 24px; top: 79px; list-style: none; color: var(--ink); font-size: 17px; line-height: 20px; }
  .services-list li { position: relative; padding-left: 24px; margin-bottom: 8px; }
  .services-list svg { position: absolute; left: 0; top: 3px; }

  .contact-band { position: absolute; left: 0; top: 339px; width: 450px; height: 74px; background: var(--green); color: var(--paper); }
  .contact-band__address { position: absolute; left: 30px; top: 6px; font-size: 14px; line-height: 18px; }
  .contact-band__title { font-size: 18px; line-height: 22px; }
  .contact-band__reach { position: absolute; left: 216px; top: 8px; font-size: 13px; line-height: 17px; }
  .contact-band__phone { font-size: 21px; line-height: 26px; font-weight: 500; }

  .back-brand { position: absolute; left: 474px; top: 30px; text-align: center; width: 90px; display: flex; flex-direction: column; align-items: center; }
  .back-brand .brand-box__mark { width: 12px; height: 12px; margin-bottom: 2px; }
  .back-brand .brand-name__short { font-size: 17px; line-height: 18px; }
  .back-brand .brand-name__long { font-size: 8px; line-height: 9px; letter-spacing: 0.2px; }
  .back-brand .brand-tagline { font-size: 5px; margin-top: 1px; }
  .back-brand .brand-phone { font-size: 7px; }

  .stamp-box { position: absolute; left: 610px; top: 25px; width: 70px; height: 74px; border: 1px solid var(--ink); }
</style>
</head>
<body>

<section class="postcard postcard--front">
  <svg class="card-art" width="704" height="545" viewBox="0 0 704 545">
    <defs>
      <linearGradient id="patioTone" x1="0" y1="0" x2="1" y2="1">
        <stop offset="0" stop-color="var(--photo-water)"/>
        <stop offset="0.2" stop-color="var(--photo-stone)"/>
        <stop offset="0.7" stop-color="var(--photo-stone)"/>
        <stop offset="1" stop-color="var(--photo-leaf)"/>
      </linearGradient>
      <linearGradient id="poolTone" x1="0" y1="0" x2="1" y2="0">
        <stop offset="0" stop-color="var(--photo-water)"/>
        <stop offset="0.6" stop-color="var(--photo-water)"/>
        <stop offset="1" stop-color="#8c7d6c"/>
      </linearGradient>
      <linearGradient id="gardenTone" x1="0" y1="0" x2="0" y2="1">
        <stop offset="0" stop-color="var(--photo-leaf)"/>
        <stop offset="1" stop-color="#9a9a94"/>
      </linearGradient>
    </defs>

    <path role="img" aria-label="Paved patio with palms and plantings beside a pool" d="M0 0 H395 C380 60 378 130 398 172 C330 195 290 250 200 268 C130 280 60 272 0 250 Z" fill="url(#patioTone)"/>

    <path role="img" aria-label="Swimming pool with stone retaining wall" d="M395 0 H704 V168 C620 146 530 140 455 160 C420 170 405 175 398 172 C378 130 380 60 395 0 Z" fill="url(#poolTone)" stroke="var(--green)" stroke-width="7"/>

    <path d="M0 250 C60 272 130 280 200 268 C290 250 330 195 398 172 C460 152 570 150 704 176 V188 C570 165 465 170 405 195 C330 228 290 292 190 304 C110 312 40 300 0 282 Z" fill="var(--green)"/>
    <path d="M0 282 C40 300 110 312 190 304 C140 322 60 318 0 300 Z" fill="var(--green-light)"/>

    <rect x="0" y="479" width="704" height="66" fill="var(--green)"/>
    <g stroke="var(--green)" stroke-width="6" fill="url(#gardenTone)">
      <circle role="img" aria-label="Stone walkway with garden beds" cx="316" cy="466" r="58"/>
      <circle role="img" aria-label="Driveway lined with evergreen shrubs" cx="459" cy="466" r="58"/>
      <circle role="img" aria-label="Curved paver path with planting bed" cx="602" cy="466" r="58"/>
    </g>
  </svg>

  <div class="headline">
    <p class="headline__lead">WE ARE A</p>
    <p class="headline__sub">LANDSCAPE MAINTENANCE,<br>DESIGN AND BUILD COMPANY.</p>
  </div>

  <p class="credentials">WE ARE A FULLY INSURED<br>NJ HOME IMPROVEMENT CONTRACTOR<br>LICENSE 27KP81926058</p>

  <div class="brand-box">
    <span class="brand-box__mark"></span>
    <p class="brand-name"><span class="brand-name__short">K&amp;R</span><span class="brand-name__long">CONTRACTING</span></p>
    <p class="brand-tagline">Landscaping - Snow Removal</p>
    <p class="brand-phone">973-555-0182</p>
  </div>
</section>

<section class="postcard postcard--back">
  <svg class="card-art" width="704" height="545" viewBox="0 0 704 545">
    <path d="M285 0 H310 C420 110 450 260 420 360 C400 430 360 500 320 545 H300 C340 495 385 430 400 360 C430 250 400 110 285 0 Z" fill="var(--green)"/>
    <path d="M300 0 H330 C440 120 460 270 430 360 C410 430 375 495 340 545 H330 C365 495 400 430 415 360 C440 260 410 110 300 0 Z" fill="var(--green-dark)"/>
  </svg>

  <h2 class="services-tab">Our Services</h2>
  <ul class="services-list">
    <li><svg width="16" height="14" viewBox="0 0 16 14"><path d="M1 7 L6 12 L15 1" stroke="var(--green)" stroke-width="2.5" fill="none"/></svg>Include Weekly Property Maintenance</li>
    <li><svg width="16" height="14" viewBox="0 0 16 14"><path d="M1 7 L6 12 L15 1" stroke="var(--green)" stroke-width="2.5" fill="none"/></svg>Spring And Fall Clean Ups</li>
    <li><svg width="16" height="14" viewBox="0 0 16 14"><path d="M1 7 L6 12 L15 1" stroke="var(--green)" stroke-width="2.5" fill="none"/></svg>Tree</li>
    <li><svg width="16" height="14" viewBox="0 0 16 14"><path d="M1 7 L6 12 L15 1" stroke="var(--green)" stroke-width="2.5" fill="none"/></svg>Shrub And Plant Care</li>
    <li><svg width="16" height="14" viewBox="0 0 16 14"><path d="M1 7 L6 12 L15 1" stroke="var(--green)" stroke-width="2.5" fill="none"/></svg>Pool Renovations And New Installations</li>
    <li><svg width="16" height="14" viewBox="0 0 16 14"><path d="M1 7 L6 12 L15 1" stroke="var(--green)" stroke-width="2.5" fill="none"/></svg>Patio And Retaining Wall Design<br>And Construction</li>
    <li><svg width="16" height="14" viewBox="0 0 16 14"><path d="M1 7 L6 12 L15 1" stroke="var(--green)" stroke-width="2.5" fill="none"/></svg>Deign And Building Of Outdoor Kitchens</li>
    <li><svg width="16" height="14" viewBox="0 0 16 14"><path d="M1 7 L6 12 L15 1" stroke="var(--green)" stroke-width="2.5" fill="none"/></svg>Fireplaces And Water Features.</li>
  </ul>

  <div class="contact-band">
    <div class="contact-band__address">
      <p class="contact-band__title">CONTACT US</p>
      <p>Address Line 1</p>
      <p>Address Line 2</p>
    </div>
    <div class="contact-band__reach">
      <p class="contact-band__phone">CALL - 973-555-0182</p>
      <p>Mail - yourmail@example.com</p>
      <p>Web - www.yourwebsite.com</p>
    </div>
  </div>

  <div class="back-brand">
    <span class="brand-box__mark"></span>
    <p class="brand-name"><span class="brand-name__short">K&amp;R</span><span class="brand-name__long">CONTRACTING</span></p>
    <p class="brand-tagline">Landscaping - Snow Removal</p>
    <p class="brand-phone">973-555-0182</p>
  </div>

  <div class="stamp-box"></div>
</section>

</body>
</html>
```